Real Estate Agent who sells beach front condos needs a template for a monthly postcard campaign.

Carla Jenrick, Homebroker with Quintavo Real Estate and Development, Licensed in Florida and Alabama, 251-468-3072, carlajenrick.example, carlamjenrick@mailbox.example. Need a postcard template which will allow me to type in recipe instructions and insert a photo of the finished food product. The recipe and photo will change every month, so I need this to be something I can easily change and reorder every month. I sell beach condos primarily. I'd like large photos of the food. Glossy card on both sides.

Target Market(s)

buyers and sellers of homes, condos, lots

Industry/Entity Type

Real Estate Agent

Requirements
Must have
• my contact information, my photo, my company name (Quintavo Real Estate and Development), the Equal Dwelling Logo, the Homebroker Logo, the statement "Contact me for all your Real Estate needs!", a template on the front side that will let me change the photograph at will, and a template on the back side that will let me type words.
Nice to have
• For my contact info and photo to stand out also.

```html
<!DOCTYPE html>
<html lang="en">
<head>
<meta charset="utf-8">
<title>Recipe Postcard – Carla Jenrick</title>
<link rel="stylesheet" href="https://fonts.googleapis.com/css2?family=Lobster+Two:ital,wght@1,400;1,700&family=Open+Sans:wght@400;600;700&family=Raleway:wght@400;500&display=swap">
<style>
  :root {
    --page: #e6e4e0;
    --yellow: #f3d22b;
    --yellow-deep: #e9c21a;
    --tan: #c9bea7;
    --white: #ffffff;
    --ink: #4a4a4a;
    --ink-soft: #6b6b6b;
    --ink-brown: #5a4a14;
    --wood-dark: #4e4236;
    --wood-light: #8a7a68;
    --tomato: #c9302c;
    --basil: #4d7a2e;
  }
  * { box-sizing: border-box; margin: 0; padding: 0; }
  html, body { width: 1200px; height: 800px; overflow: hidden; }
  body {
    background: var(--page);
    font-family: "Open Sans", Arial, sans-serif;
    display: flex;
    align-items: center;
    justify-content: center;
    gap: 40px;
  }
  .postcard {
    position: relative;
    width: 550px;
    height: 350px;
    overflow: hidden;
    background: var(--white);
    box-shadow: 0 6px 18px rgba(0,0,0,.18);
  }

  /* ---------- Back side ---------- */
  .ingredients {
    position: absolute; left: 0; top: 0;
    width: 140px; height: 245px;
    background: var(--tan);
    padding: 14px 12px;
  }
  .ingredients__title {
    font-family: "Lobster Two", "Brush Script MT", cursive;
    font-style: italic;
    font-weight: 400;
    color: var(--white);
    font-size: 19px;
    margin-bottom: 8px;
  }
  .ingredients__list { list-style: none; }
  .ingredients__list li {
    font-size: 7.5px;
    line-height: 1.55;
    color: var(--white);
    font-style: italic;
  }
  .preparation {
    position: absolute; left: 140px; top: 0;
    width: 410px; height: 245px;
    padding: 14px 20px;
  }
  .preparation__title {
    font-family: "Lobster Two", "Brush Script MT", cursive;
    font-style: italic;
    font-weight: 700;
    color: var(--yellow-deep);
    font-size: 28px;
    margin-bottom: 14px;
  }
  .preparation__steps p {
    font-size: 8.5px;
    line-height: 1.6;
    color: var(--ink-soft);
    width: 260px;
    margin-bottom: 9px;
  }
  .utensils-art {
    position: absolute; right: 18px; top: 10px;
    width: 90px; height: 70px;
    background: linear-gradient(135deg, #fbf2c4, #f6e58a);
    border-radius: 4px;
  }
  .contact-band {
    position: absolute; left: 0; bottom: 0;
    width: 100%; height: 105px;
    background: var(--yellow);
  }
  .agent-photo {
    position: absolute; left: 22px; bottom: 14px;
    width: 110px; height: 110px;
    border-radius: 50%;
    border: 5px solid var(--yellow);
    background: radial-gradient(circle at 50% 40%, #e9d8b6, #b89c74);
  }
  .agent-details {
    position: absolute; left: 165px; top: 14px;
    width: 235px;
    color: var(--ink);
  }
  .agent-details__name {
    font-size: 14px; font-weight: 600; color: var(--ink-brown); margin-bottom: 3px;
  }
  .agent-details__line { font-size: 8px; line-height: 1.5; }
  .agent-details__contact { font-size: 8px; line-height: 1.6; margin-top: 7px; }

  .agent-extras {
    position: absolute; left: 408px; top: 14px;
    width: 126px;
  }
  .agent-extras__statement {
    font-size: 9px; font-weight: 700; line-height: 1.35;
    color: var(--ink-brown);
    margin-bottom: 10px;
  }
  .badge-row { display: flex; flex-direction: column; gap: 6px; }
  .badge {
    display: flex; align-items: center; gap: 6px;
    font-size: 8px; font-weight: 600; color: var(--ink-brown);
  }
  .badge__mark {
    width: 14px; height: 14px;
    background: var(--white);
    flex: none;
  }
  .badge__mark--circle { border-radius: 50%; }

  /* ---------- Front side ---------- */
  .front-photo {
    position: absolute; inset: 0;
    background:
      radial-gradient(ellipse at 20% 18%, rgba(201,48,44,.75), transparent 38%),
      radial-gradient(ellipse at 70% 15%, rgba(77,122,46,.6), transparent 35%),
      radial-gradient(ellipse at 90% 5%, rgba(190,40,40,.55), transparent 30%),
      linear-gradient(180deg, var(--wood-light), var(--wood-dark));
  }
  .crop-line-v {
    position: absolute; left: 200px; top: 0; bottom: 0;
    width: 1px; background: rgba(255,255,255,.85);
  }
  .recipe-badge {
    position: absolute; left: 169px; top: 62px;
    width: 62px; height: 62px;
    border-radius: 50%;
    background: var(--yellow);
    color: var(--white);
    font-size: 12px; font-weight: 600;
    display: flex; align-items: center; justify-content: center;
  }
  .title-band {
    position: absolute; left: 200px; right: 0; top: 150px;
    height: 72px;
    background: rgba(255,255,255,.72);
    padding: 6px 14px;
  }
  .title-band__title {
    font-family: "Lobster Two", "Brush Script MT", cursive;
    font-style: italic;
    color: var(--yellow-deep);
    font-size: 40px;
    line-height: 1.1;
    white-space: nowrap;
  }
  .title-band__subtitle {
    font-family: "Raleway", Arial, sans-serif;
    font-size: 9.5px;
    letter-spacing: .04em;
    color: var(--ink-soft);
    text-transform: uppercase;
    white-space: nowrap;
  }
</style>
</head>
<body>

  <section class="postcard postcard--back" aria-label="Postcard back">
    <div class="ingredients">
      <h2 class="ingredients__title">Ingredients</h2>
      <ul class="ingredients__list">
        <li>250g couscous</li>
        <li>zest and juice 1 lemon</li>
        <li>2 tbsp olive oil</li>
        <li>2 tbsp tahini paste</li>
        <li>1 garlic clove, crushed</li>
        <li>2 courgettes, sliced</li>
        <li>4 tomatoes, roughly chopped</li>
        <li>200g feta, crumbled</li>
        <li>small pack parsley</li>
        <li>1 red chilli, sliced</li>
      </ul>
    </div>

    <div class="preparation">
      <h2 class="preparation__title">Preparation</h2>
      <div class="preparation__steps">
        <p>Put the couscous in a heatproof bowl and pour over boiling water to just cover.</p>
        <p>Cover with cling film and leave to stand for 5 mins.</p>
        <p>Mix the lemon zest and juice, oil, tahini and garlic, and season to taste. Fluff the prepared couscous and season. Spoon onto a large serving platter and scatter over the courgettes, tomatoes, feta, herbs and chilli. Drizzle over the dressing.</p>
      </div>
      <div class="utensils-art" role="img" aria-label="Line drawing of kitchen whisks and utensils"></div>
    </div>

    <div class="contact-band">
      <div class="agent-photo" role="img" aria-label="Portrait photo of Carla Jenrick"></div>
      <div class="agent-details">
        <p class="agent-details__name">Carla Jenrick</p>
        <p class="agent-details__line">Homebroker with Quintavo Real Estate and Development.</p>
        <p class="agent-details__line">Licensed in Florida and Alabama.</p>
        <p class="agent-details__contact">T: 251-468-3072<br>E: carlamjenrick@mailbox.example<br>W: carlajenrick.example</p>
      </div>
      <div class="agent-extras">
        <p class="agent-extras__statement">Contact me for all your Real Estate needs!</p>
        <div class="badge-row">
          <span class="badge"><span class="badge__mark"></span>Equal Dwelling</span>
          <span class="badge"><span class="badge__mark badge__mark--circle"></span>Homebroker</span>
        </div>
      </div>
    </div>
  </section>

  <section class="postcard postcard--front" aria-label="Postcard front">
    <div class="front-photo" role="img" aria-label="Photo of tomatoes, basil, garlic, olives, olive oil and spaghetti on a wooden table"></div>
    <div class="crop-line-v"></div>
    <div class="recipe-badge">Recipe 1</div>
    <div class="title-band">
      <h1 class="title-band__title">Italian caserole</h1>
      <p class="title-band__subtitle">A refreshing summer dish for the whole family</p>
    </div>
  </section>

</body>
</html>
```